WP website design Pine Harbor (Contest)

We need a wordpress design that will incorporate a professional color scheme with company logo in a clean layout. The design needs to consider that this will be developed on a responsive theme. Colors are blue and green of the logo and and an accent color (perhaps very light brown/tan). Client wants a 'modern' look.

Industry/Entity Type

It Company

Font styles to use
Serif
Sans Serif

Colors

Designer to choose colors to be used in the design.

Requirements
Must have
• Navigation: 1) Home; 2) Upcoming Auctions; 3) Past Auctions; 4) About Us; 5) Services; 6) Sellers; 7) Buyers; 8) Contact Us

Site will have slideshow - image is attached. Colors will be those in the logo, blue and green with maybe an accent color. A site the client mentions liking is trevalleauctions.com for the use of color and layout.

Widgets: 1) Featured Properties; 2) Call to action for Sellers 3) Testimonials blog/widget
Nice to have
• use of dropdown menus

```html
<!DOCTYPE html>
<html lang="en">
<head>
<meta charset="utf-8">
<title>Pine Harbor Auction &amp; Real Estate</title>
<link href="https://fonts.googleapis.com/css2?family=Titillium+Web:wght@400;600;700&display=swap" rel="stylesheet">
<style>
:root{
  --navy:#0b3a74;
  --navy-dark:#062f63;
  --nav-top:#0d5aa0;
  --nav-bottom:#073a75;
  --green:#0c6b3a;
  --green-bright:#118a47;
  --heading-blue:#0d3f7a;
  --title-green:#138a3c;
  --grey-band:#e6e6e6;
  --text:#555;
  --dark:#222;
  --white:#fff;
}
*{margin:0;padding:0;box-sizing:border-box}
html,body{width:692px;height:1200px;overflow:hidden;background:var(--white)}
body{position:relative;font-family:"Titillium Web",Arial,sans-serif;color:var(--dark)}
.abs{position:absolute}
.top-rule{left:0;top:0;width:692px;height:2px;background:var(--navy)}
.brand{left:58px;top:24px;display:flex;align-items:center;gap:6px}
.brand-dot{width:22px;height:22px;border-radius:50%;background:var(--navy)}
.brand-name{font-size:15px;font-weight:700;color:var(--navy);line-height:1}
.brand-rule{left:58px;top:71px;width:93px;height:1px;background:var(--green)}
.tagline{left:159px;top:24px;font-size:13px;font-weight:700;color:var(--title-green);line-height:14px;text-align:center}
.phones{left:528px;top:29px;display:flex;align-items:center;gap:14px}
.phones ul{list-style:none;font-size:10.5px;font-weight:600;line-height:17px;color:var(--dark)}
.nav{left:0;top:84px;width:692px;height:43px;background:linear-gradient(var(--nav-top),var(--nav-bottom))}
.nav ul{list-style:none;display:flex;margin-left:58px;height:43px}
.nav li{font-size:7.8px;font-weight:600;color:var(--white);line-height:43px;padding:0 13.5px}
.nav li.active{background:var(--green);padding:0 20px}
.hero{left:0;top:127px;width:692px;height:310px;background:linear-gradient(#5d7a4f 0%,#8c6b5a 12%,#9c7866 30%,#7b8b4a 40%,#8aa3c4 48%,#6b8f45 56%,#3f8a2b 75%,#2f7a22 100%)}
.hero-title{left:57px;top:236px;font-size:20px;font-weight:600;color:var(--white);line-height:28px}
.hero-arrow{top:252px}
.dots{left:325px;top:419px;display:flex;gap:4px}
.dots span{width:8px;height:8px;border-radius:50%;background:var(--white);border:1px solid #bbb}
.dots span.on{background:var(--navy)}
.section-title{width:692px;left:0;text-align:center;font-size:14px;font-weight:600;color:var(--heading-blue)}
.welcome-text{left:57px;top:473px;width:578px;text-align:center;font-size:6.6px;line-height:13.6px;color:var(--text)}
.band{left:0;width:692px;background:var(--grey-band)}
.card{top:573px;width:184px;height:204px;background:var(--white);box-shadow:0 3px 4px rgba(0,0,0,.18)}
.card-img{height:111px;border-top:3px solid var(--navy)}
.card h3{font-size:9.5px;font-weight:600;color:var(--title-green);text-align:center;margin-top:6px}
.card p{font-size:6.6px;line-height:11.8px;color:var(--text);text-align:center;padding:0 8px;margin-top:2px}
.card-foot{position:absolute;left:0;bottom:0;width:100%;height:26px;border-top:1px solid #ddd;display:flex;align-items:center;justify-content:space-between;padding:0 7px;font-size:7px;font-weight:600}
.card-foot .meta{color:#aaa;font-weight:400;display:flex;gap:5px;align-items:center}
.promo{top:824px;width:144px;height:102px}
.promo-text{padding:9px 8px;color:var(--white)}
.promo-text h3{font-size:10.5px;font-weight:600;margin-bottom:3px}
.promo-text p{font-size:6.8px;font-weight:600;line-height:11px}
.testi-title{left:57px;top:955px;font-size:14px;font-weight:600;color:var(--heading-blue)}
.testi-img{top:983px;width:185px;height:89px}
.avatar{width:52px;height:52px;border-radius:50%;border:3px solid var(--white);background:#b88d76}
.testi-meta{font-size:6.6px;color:var(--text)}
.testi-head{font-size:7.6px;font-weight:600;color:var(--dark)}
.cta{left:458px;top:983px;width:176px;height:117px;background:linear-gradient(#3b4d5e,#5c6a72 60%,#45504a);text-align:center}
.cta h3{font-size:12px;font-weight:600;color:var(--white);margin-top:40px}
.cta .btn{display:inline-block;margin-top:5px;width:72px;height:18px;line-height:18px;background:var(--green-bright);color:var(--white);font-size:7.5px;font-weight:600}
.footer{left:0;top:1120px;width:692px;height:80px;background:var(--navy-dark);color:var(--white)}
.footer-links{left:58px;top:17px;font-size:7px}
.footer-copy{left:58px;top:31px;font-size:7px}
.socials{left:58px;top:48px;display:flex;gap:5px}
.socials span{width:14px;height:14px;background:#3d6fb0;border-radius:2px}
.socials span.rss{background:#e07b23}
.signup{left:513px;top:17px;font-size:8px;font-weight:600}
.signup-form{left:513px;top:36px;display:flex}
.signup-form .field{width:86px;height:18px;background:var(--white);color:#333;font-size:6.5px;line-height:18px;padding-left:4px}
.signup-form .send{width:36px;height:18px;background:var(--green-bright);font-size:7px;font-weight:600;text-align:center;line-height:18px}
</style>
</head>
<body>
<div class="abs top-rule"></div>

<header>
  <div class="abs brand"><span class="brand-dot"></span><span class="brand-name">Harborline<br>Realty</span></div>
  <div class="abs brand-rule"></div>
  <div class="abs tagline">Pine Harbor<br>Auction &amp;<br>Real Estate</div>
  <div class="abs phones">
    <svg width="16" height="14" viewBox="0 0 16 14" aria-hidden="true"><path d="M1 4 Q8 -1 15 4 L13 6 L11 4.5 L11 3 Q8 2 5 3 L5 4.5 L3 6 Z" fill="#222"/><path d="M4 6 L12 6 L14 13 L2 13 Z" fill="#222"/><circle cx="8" cy="9.5" r="2" fill="#fff"/></svg>
    <ul><li>(555) 014-3829</li><li>(555) 016-7204</li></ul>
  </div>
</header>

<nav class="abs nav">
  <ul>
    <li class="active">Home</li><li>Upcoming Auctions</li><li>Past Auctions</li><li>About Us</li><li>Services</li><li>Buyers</li><li>Sellers</li><li>About Us</li><li>Contact Us</li>
  </ul>
</nav>

<section class="abs hero" role="img" aria-label="Slideshow photo of farmland with a crop field, a pond and green soybean rows"></section>
<h1 class="abs hero-title">HARBORLINE<br>REALTY</h1>
<svg class="abs hero-arrow" style="left:22px" width="12" height="20" viewBox="0 0 12 20" aria-hidden="true"><path d="M10 1 L2 10 L10 19" stroke="#0d3f7a" stroke-width="4" fill="none"/></svg>
<svg class="abs hero-arrow" style="left:652px" width="12" height="20" viewBox="0 0 12 20" aria-hidden="true"><path d="M2 1 L10 10 L2 19" stroke="#0d3f7a" stroke-width="4" fill="none"/></svg>
<div class="abs dots"><span class="on"></span><span></span><span></span></div>

<section>
  <h2 class="abs section-title" style="top:450px">Welcome To Harborline Realty</h2>
  <p class="abs welcome-text">Lorem ipsum dolor sit amet, consectetuer adipiscing elit, sed diam nonummy nibh euismod tincidunt ut laoreet dolore magna aliquam erat volutpat. Ut wisi enim ad minim veniam, quis nostrud exerci tation ullamcorper suscipit lobortis nisl ut aliquip ex ea commodo consequat. Lorem ipsum dolor sit amet, consectetuer adipiscing elit, sed diam nonummy nibh euismod tincidunt ut laoreet dolore magna aliquam erat volutpat. Ut wisi enim ad minim veniam, quis nostrud exerci tation ullamcorper</p>
</section>

<section class="abs band" style="top:524px;height:276px"></section>
<h2 class="abs section-title" style="top:543px">Featured Properties</h2>

<article class="abs card" style="left:57px">
  <div class="card-img" role="img" aria-label="Photo of a white two-storey house with red shutters" style="background:linear-gradient(#3b6fb5,#9bb8d8 45%,#4f7a3a 75%,#3a6a2a)"></div>
  <h3>Lorem Ipsum</h3>
  <p>Lorem ipsum dolor sit amet, consectetuer adipisc-ing elit, sed diam nonummy nibh euismod tincidunt ut laoreet dolore magna</p>
  <div class="card-foot"><span>Area : 240m²</span><span class="meta">▬ 4 ▲ 5</span></div>
</article>
<article class="abs card" style="left:253px">
  <div class="card-img" role="img" aria-label="Photo of a stone house among bare trees" style="background:linear-gradient(#8fb2d6,#c9d6e2 40%,#7d7b6e 65%,#4e7a34)"></div>
  <h3>Lorem Ipsum</h3>
  <p>Lorem ipsum dolor sit amet, consectetuer adipisc-ing elit, sed diam nonummy nibh euismod tincidunt ut laoreet dolore magna</p>
  <div class="card-foot"><span>Area : 240m²</span><span class="meta">▬ ▲ 5</span></div>
</article>
<article class="abs card" style="left:449px">
  <div class="card-img" role="img" aria-label="Photo of a yellow farmhouse with a white porch" style="background:linear-gradient(#d2c08e,#c9b98c 50%,#e6e2d4 70%,#5e8a3a)"></div>
  <h3>Lorem Ipsum</h3>
  <p>Lorem ipsum dolor sit amet, consectetuer adipisc-ing elit, sed diam nonummy nibh euismod tincidunt ut laoreet dolore magna</p>
  <div class="card-foot"><span>Area : 240m²</span><span class="meta">▬ ▲ 5</span></div>
</article>

<section>
  <div class="abs promo" style="left:58px;background:var(--navy)">
    <div class="promo-text"><h3>Buyer</h3><p>Lorem ipsum dolor sit amet, consec-tetuer adipiscing elit, sed diam nonummy nibh euismod tincidunt ut laoreet dolore magna aliquam erat volutpat.<br>Read more..</p></div>
  </div>
  <div class="abs promo" style="left:202px;background:linear-gradient(#7aa7d8,#c8835e 45%,#8d6b55 70%,#6b7f4a)" role="img" aria-label="Photo of a modern house with a red tile roof"></div>
  <div class="abs promo" style="left:346px;background:var(--green)">
    <div class="promo-text"><h3>Seller</h3><p>Lorem ipsum dolor sit amet, consec-tetuer adipiscing elit, sed diam nonummy nibh euismod tincidunt ut laoreet dolore magna aliquam erat volutpat.<br>Read more..</p></div>
  </div>
  <div class="abs promo" style="left:490px;background:linear-gradient(135deg,#f2f2f2,#dfe4ea 55%,#c9ced6)" role="img" aria-label="Photo of hands reviewing charts on a tablet"></div>
</section>

<section class="abs band" style="top:940px;height:180px"></section>
<h2 class="abs testi-title">Testimonials blog/widget</h2>

<div class="abs testi-img" style="left:57px;background:linear-gradient(#5d8fcf,#b0c8e4 35%,#7a4a2e 60%,#4e6a34)" role="img" aria-label="Photo of a log cabin house"></div>
<div class="abs avatar" style="left:120px;top:1031px" role="img" aria-label="Portrait of a customer"></div>
<div class="abs testi-meta" style="left:57px;top:1085px">Aug 9, 2013 &nbsp;3 comments</div>
<div class="abs testi-head" style="left:57px;top:1097px">Lorem ipsum dolor sit amet</div>

<div class="abs testi-img" style="left:253px;width:184px;background:linear-gradient(120deg,#e0b9a2,#f1f1f1 50%,#c9d5e5)" role="img" aria-label="Photo of a hand holding a key and a small model house"></div>
<div class="abs avatar" style="left:314px;top:1031px;background:#8f7a6e" role="img" aria-label="Portrait of a customer"></div>
<div class="abs testi-meta" style="left:253px;top:1085px">Aug 9, 2013 &nbsp;3 comments</div>
<div class="abs testi-head" style="left:253px;top:1097px">Lorem ipsum dolor sit amet</div>

<aside class="abs cta" role="img" aria-label="Photo of a suburban house at dusk behind the call to action">
  <h3>Call to action for Sellers</h3>
  <span class="btn">CLICK HERE</span>
</aside>

<footer class="abs footer">
  <div class="abs footer-links">Home &nbsp;| &nbsp;About Us &nbsp;| &nbsp;Products &nbsp;| &nbsp;Contact Us</div>
  <div class="abs footer-copy">© 2014 Company Name &nbsp;All right reserved &nbsp;Term of Use</div>
  <div class="abs socials"><span></span><span></span><span></span><span class="rss"></span></div>
  <div class="abs signup">Email Sign Up</div>
  <div class="abs signup-form"><span class="field">Email address</span><span class="send">Send</span></div>
</footer>
</body>
</html>
```